Clean Vormix Ads Banner Design For A Finance Company

Hi,
We're a UK based finance company and are looking for new banner ads to use on the Vormix Display Network.
We want the end product to stand out by using strong, minimal design - ideally starting from a dark theme, although I'm open to ideas.
The copy should read:
'Fast Bridging Loans From 0.39% PM'
Once we have these designs agreed, we are looking to replicate them for other products, changing only the text on each ad - for example, 'commercial mortgage service you can rely on' or 'development finance service you can rely on'.
The colours used on our website are the following:
Black - #040303
Orange - #f79124
White - #ffffff
Grey - #ffffff
Example ads that I like - https://www.plexabyte.com/wp-content/uploads/2021/07/vormix-display-ads-example-2-final.png.webp
2 - https://adquilterhub.com/wp-content/uploads/2020/03/fbdd56ba3bd16c7a8debb13a411de786.jpg

```html
<!DOCTYPE html>
<html lang="en">
<head>
<meta charset="utf-8">
<title>Fast Bridging Loans – Banner Set</title>
<link rel="stylesheet" href="https://fonts.googleapis.com/css2?family=Saira:ital,wght@0,400;0,500;0,600;1,700;1,800&display=swap">
<style>
  :root {
    --board: #c0c0c0;
    --black: #040303;
    --orange: #f79124;
    --white: #ffffff;
    --grey-band: #6b6e72;
    --deep-orange: #ff5a00;
  }
  * { margin: 0; padding: 0; box-sizing: border-box; }
  html, body { width: 1200px; height: 1200px; overflow: hidden; }
  body {
    position: relative;
    background: var(--board);
    font-family: "Saira", "Arial Narrow", sans-serif;
    color: var(--white);
  }

  /* Shared */
  .headline { font-style: italic; font-weight: 800; line-height: 1; letter-spacing: 0.5px; }
  .headline .accent { color: var(--orange); }
  .rate-intro { font-weight: 500; line-height: 1; }
  .rate-value { font-weight: 600; line-height: 1; }
  .rate-unit { font-weight: 500; }
  .cta {
    position: absolute;
    display: flex; align-items: center; justify-content: center;
    background: var(--white);
    color: var(--black);
    border-radius: 999px;
    font-weight: 500;
    letter-spacing: 1px;
    text-transform: uppercase;
  }
  .artwork { position: absolute; }
  .brand-name { font-weight: 600; line-height: 1.05; }

  /* Skyscraper banner */
  .banner-tall {
    position: absolute;
    left: 388px; top: 45px;
    width: 425px; height: 850px;
    background: var(--black);
    overflow: hidden;
    box-shadow: 6px 8px 14px rgba(0,0,0,0.35);
  }
  .banner-tall .brand-tab {
    position: absolute;
    left: 272px; top: 0;
    width: 106px; height: 76px;
    background: var(--white);
    border-radius: 0 0 10px 10px;
    display: flex; align-items: center; justify-content: center;
    text-align: center;
  }
  .banner-tall .brand-name { color: var(--black); font-size: 15px; }
  .banner-tall .headline { position: absolute; left: 46px; font-size: 71px; }
  .banner-tall .line-fast { top: 88px; }
  .banner-tall .line-bridging { top: 160px; }
  .banner-tall .line-loans { top: 231px; }
  .banner-tall .rate-intro { position: absolute; left: 45px; top: 302px; font-size: 43px; }
  .banner-tall .rate-value { position: absolute; left: 44px; top: 350px; font-size: 76px; }
  .banner-tall .rate-unit { font-size: 42px; margin-left: 8px; }
  .banner-tall .artwork {
    left: 0; top: 476px; width: 425px; height: 374px;
    background:
      radial-gradient(ellipse 40% 45% at 52% 40%, #ff8a10 0%, #ff5a00 40%, rgba(120,30,0,0.6) 70%, transparent 90%),
      linear-gradient(160deg, #5e6165 0%, #2a2b2e 45%, #0d0d0f 100%);
  }
  .banner-tall .cta {
    left: 120px; top: 749px; width: 183px; height: 48px;
    font-size: 18px;
    box-shadow: 0 0 0 4px rgba(120,120,120,0.6);
  }

  /* Leaderboard banner */
  .banner-wide {
    position: absolute;
    left: 0; top: 939px;
    width: 1200px; height: 261px;
    background: var(--black);
    overflow: hidden;
  }
  .banner-wide .artwork {
    left: 620px; top: 0; width: 580px; height: 261px;
    background:
      radial-gradient(ellipse 32% 60% at 40% 45%, #ff8a10 0%, #ff5a00 40%, rgba(120,30,0,0.6) 70%, transparent 90%),
      linear-gradient(155deg, transparent 0%, #5e6165 30%, #2a2b2e 60%, #0d0d0f 100%);
  }
  .banner-wide .headline { position: absolute; left: 65px; top: 40px; font-size: 52px; white-space: nowrap; }
  .banner-wide .rate-line { position: absolute; left: 63px; top: 100px; white-space: nowrap; line-height: 1; }
  .banner-wide .rate-intro { font-size: 49px; }
  .banner-wide .rate-value { font-size: 61px; margin-left: 10px; }
  .banner-wide .rate-unit { font-size: 45px; margin-left: 6px; }
  .banner-wide .cta { left: 65px; top: 173px; width: 188px; height: 42px; font-size: 19px; }
  .banner-wide .brand-lockup {
    position: absolute; left: 1040px; top: 172px; width: 140px;
    text-align: center;
  }
  .banner-wide .brand-name { color: var(--orange); font-size: 22px; }
</style>
</head>
<body>

  <section class="banner-tall" aria-label="Skyscraper banner">
    <div class="brand-tab"><span class="brand-name">Kestrel<br>Finance Limited</span></div>
    <h1 class="headline line-fast"><span class="accent">FAST</span></h1>
    <div class="headline line-bridging">BRIDGING</div>
    <div class="headline line-loans">LOANS</div>
    <p class="rate-intro">From</p>
    <p class="rate-value">0.39%<span class="rate-unit">PM</span></p>
    <div class="artwork" role="img" aria-label="Isometric illustration of a glowing orange puzzle piece bridging a gap between dark grey puzzle blocks"></div>
    <a class="cta">Apply Now</a>
  </section>

  <section class="banner-wide" aria-label="Leaderboard banner">
    <div class="artwork" role="img" aria-label="Isometric illustration of a glowing orange puzzle piece bridging a gap between dark grey puzzle blocks"></div>
    <h2 class="headline"><span class="accent">FAST</span> BRIDGING LOANS</h2>
    <p class="rate-line"><span class="rate-intro">From</span><span class="rate-value">0.39%</span><span class="rate-unit">PM</span></p>
    <a class="cta">Apply Now</a>
    <div class="brand-lockup"><span class="brand-name">Kestrel<br>Finance Limited</span></div>
  </section>

</body>
</html>
```